I need a business card design for my new clinic (SPORTS MEDICINE OF KNEE). I am orthopedist, expert in sports surgery, especially knee surgery. I prefer, as colors, the colors of my logo (green, black and white). I already have my logo and should appear on my card. It's good to see my site to have ideas (www.drlucianovarela.com)
It needs contain:
my name: Dr. Luciano Varela
my registration: CRM 584-902
my specialty: Cirurgia do Joelho / Esporte
my address: Centro Executivo - Pinheiral Plaza
Av. Doutor Augusto Brandão Cunha, 2740 sala 0836
Jd. Ipanema - Ribeirão Preto - SP
my phone number: Tel (16) 8245-3908
my clinic phone: (16) 3670-4851
my e-mail: drlucianovarela@mailbox-exemplo.com
my site: www.drlucianovarela.com

Target Market(s)

futures patients

Industry/Entity Type

Clinic

Requirements
Nice to have
• letters not overfilled
straight lines, with few curves

```html
<!DOCTYPE html>
<html lang="pt">
<head>
<meta charset="utf-8">
<title>Varela Traumatologia Esportiva – Cartão de Visita</title>
<link rel="stylesheet" href="https://fonts.googleapis.com/css2?family=Tinos:wght@400;700&family=Arimo:wght@400&display=swap">
<style>
  :root {
    --backdrop: #e6d2b0;
    --card-dark: #333333;
    --card-light: #fdfdfd;
    --brand-green: #3fb56e;
    --ink: #111111;
    --paper-white: #ffffff;
    --line-grey: #d4d4d4;
  }
  * { box-sizing: border-box; margin: 0; padding: 0; }
  html, body {
    width: 1200px; height: 1000px; overflow: hidden;
    background: var(--backdrop);
  }
  .canvas { position: relative; width: 1200px; height: 1000px; }

  .card {
    position: absolute; left: 303px; width: 594px; height: 350px;
    box-shadow: 0 3px 10px rgba(0,0,0,0.28);
    font-family: "Tinos", "Times New Roman", serif;
  }

  /* Front */
  .card-front { top: 137px; background: var(--card-dark); }
  .edge-band { position: absolute; top: 0; bottom: 0; background: var(--brand-green); }
  .edge-band--left { left: 0; width: 15px; }
  .edge-band--right { right: 0; width: 17px; }

  .brand { position: absolute; }
  .brand-mark {
    position: absolute; border-radius: 6px; background: var(--brand-green);
  }
  .brand-name {
    position: absolute; white-space: nowrap; font-weight: 400; line-height: 1;
  }
  .brand-tagline {
    position: absolute; white-space: nowrap; color: var(--brand-green);
    letter-spacing: 0.06em; line-height: 1;
  }

  .card-front .brand-mark { left: 144px; top: 139px; width: 76px; height: 72px; border: 3px solid var(--paper-white); }
  .card-front .brand-name { left: 236px; top: 143px; font-size: 58px; color: var(--paper-white); }
  .card-front .brand-tagline { left: 244px; top: 195px; font-size: 16px; }

  .website {
    position: absolute; left: 0; right: 0; top: 297px; text-align: center;
    color: var(--paper-white); font-size: 17px;
  }

  /* Back */
  .card-back { top: 512px; background: var(--card-light); color: var(--ink); }
  .knee-art {
    position: absolute; left: 252px; top: 0; width: 276px; height: 349px;
    background: linear-gradient(160deg, #f6f6f6 0%, #ececec 50%, #f8f8f8 100%);
    border-left: 1px solid var(--line-grey);
  }
  .card-back .brand-mark { left: 22px; top: 22px; width: 58px; height: 55px; border: 2px solid var(--ink); }
  .card-back .brand-name { left: 92px; top: 24px; font-size: 44px; color: var(--ink); }
  .card-back .brand-tagline { left: 97px; top: 64px; font-size: 13px; }

  .doctor {
    position: absolute; right: 23px; top: 22px; text-align: right; line-height: 1;
  }
  .doctor-name { font-size: 21px; font-weight: 700; }
  .doctor-crm { font-size: 17px; font-weight: 700; margin-top: 9px; }
  .doctor-specialty { font-family: "Arimo", Arial, sans-serif; font-size: 11.5px; margin-top: 11px; }
  .doctor-phone { font-size: 13px; margin-top: 8px; }

  .contact { position: absolute; left: 20px; top: 224px; line-height: 1; }
  .address-line { font-size: 13.5px; font-weight: 700; margin-bottom: 3.5px; }
  .clinic-phone { font-size: 17px; font-weight: 700; margin-top: 10px; }
  .clinic-email { font-size: 17px; font-weight: 700; margin-top: 10px; }
</style>
</head>
<body>
<div class="canvas">

  <section class="card card-front">
    <div class="edge-band edge-band--left"></div>
    <div class="edge-band edge-band--right"></div>
    <div class="brand">
      <div class="brand-mark"></div>
      <div class="brand-name">VARELA</div>
      <div class="brand-tagline">Traumatologia Esportiva</div>
    </div>
    <div class="website">www.drlucianovarela.com</div>
  </section>

  <section class="card card-back">
    <div class="knee-art" role="img" aria-label="Faint outline illustration of a knee joint"></div>
    <div class="brand">
      <div class="brand-mark"></div>
      <div class="brand-name">VARELA</div>
      <div class="brand-tagline">Traumatologia Esportiva</div>
    </div>
    <div class="doctor">
      <div class="doctor-name">Dr. Luciano Varela</div>
      <div class="doctor-crm">CRM 584-902</div>
      <div class="doctor-specialty">Cirurgia do Joelho / Esporte</div>
      <div class="doctor-phone">(16) 8245-3908</div>
    </div>
    <div class="contact">
      <div class="address-line">Centro Executivo - Pinheiral Plaza</div>
      <div class="address-line">Av. Doutor Augusto Brandão Cunha, 2740 sala 0836</div>
      <div class="address-line">Jd. Ipanema - Ribeirão Preto - SP</div>
      <div class="clinic-phone">(16) 3670-4851</div>
      <div class="clinic-email">drlucianovarela@mailbox-exemplo.com</div>
    </div>
  </section>

</div>
</body>
</html>
```